Q7M Electrical Systems Inc Business Cards

Target Market(s)

Customers

Industry/Entity Type

Construction - Electrical

Contact Information for Business Card

Company Name, Address, Phone, and email address

Font styles to use
Sans Serif

Colors
0054AA
0677BA
7BADD7
CADEEF
E8F1F8

Requirements
Must have
• we would like to use the same design that we had our vehicles wrapped
Nice to have
• The design that we used on our trucks

```html
<!DOCTYPE html>
<html lang="en">
<head>
<meta charset="utf-8">
<title>Q7M Electrical Systems Inc – Business Cards</title>
<link rel="stylesheet" href="https://fonts.googleapis.com/css2?family=Poppins:ital,wght@0,400;0,600;0,700;1,300;1,400&display=swap">
<style>
  :root {
    --navy: #132334;
    --steel: #9a9a9a;
    --paper: #ffffff;
    --backdrop: #e6e6e6;
  }
  * { margin: 0; padding: 0; box-sizing: border-box; }
  html, body { width: 1200px; height: 1000px; overflow: hidden; }
  body {
    background: var(--backdrop);
    font-family: "Poppins", Arial, sans-serif;
    position: relative;
  }
  .card {
    position: absolute;
    left: 300px;
    width: 600px;
    height: 364px;
    border-radius: 32px;
    overflow: hidden;
    background: var(--navy);
  }
  .card--front { top: 108px; }
  .card--back { top: 528px; }
  .card__art { position: absolute; inset: 0; }

  .services {
    position: absolute;
    left: 42px;
    top: 52px;
    list-style: none;
  }
  .services li {
    display: flex;
    align-items: center;
    gap: 5px;
    height: 32.5px;
    font-size: 26px;
    font-style: italic;
    font-weight: 300;
    color: var(--navy);
  }
  .services svg { width: 26px; height: 26px; flex: none; }

  .brand {
    position: absolute;
    text-align: center;
    color: var(--steel);
    font-weight: 600;
    line-height: 1.1;
  }
  .brand__name { font-size: 44px; letter-spacing: 1px; }
  .brand__sub { font-size: 17px; letter-spacing: 2px; text-transform: uppercase; }

  .card--front .brand { left: 346px; width: 207px; top: 160px; }
  .brand-rule {
    position: absolute;
    left: 346px; top: 286px;
    width: 207px; height: 2px;
    background: var(--steel);
  }
  .web {
    position: absolute;
    left: 346px; width: 207px; top: 309px;
    text-align: center;
    font-size: 20px;
    font-style: italic;
    color: var(--steel);
  }

  .card--back .brand { left: 0; width: 600px; top: 58px; }
  .contact {
    position: absolute;
    left: 0; width: 600px; top: 248px;
    text-align: center;
    color: var(--steel);
  }
  .contact__address { font-size: 14px; font-style: italic; line-height: 1.25; }
  .contact__phone {
    margin-top: 8px;
    font-size: 25px;
    font-weight: 700;
    display: flex; align-items: center; justify-content: center; gap: 6px;
    line-height: 1.1;
  }
  .contact__phone svg { width: 20px; height: 20px; }
  .contact__email { font-size: 20px; line-height: 1.2; }
</style>
</head>
<body>

<section class="card card--front" aria-label="Business card front">
  <svg class="card__art" viewBox="0 0 600 364" aria-hidden="true">
    <path d="M0,0 L368,0 C300,200 200,330 68,364 L0,364 Z" fill="var(--steel)"/>
    <path d="M0,0 L324,0 C270,190 170,320 32,364 L0,364 Z" fill="var(--paper)"/>
  </svg>
  <ul class="services">
    <li><svg viewBox="0 0 26 26"><rect x="1.5" y="5.5" width="18" height="18" fill="none" stroke="#132334" stroke-width="2.5"/><path d="M5 14 L10 20 L24 3" fill="none" stroke="#132334" stroke-width="4"/></svg>Residential</li>
    <li><svg viewBox="0 0 26 26"><rect x="1.5" y="5.5" width="18" height="18" fill="none" stroke="#132334" stroke-width="2.5"/><path d="M5 14 L10 20 L24 3" fill="none" stroke="#132334" stroke-width="4"/></svg>Commercial</li>
    <li><svg viewBox="0 0 26 26"><rect x="1.5" y="5.5" width="18" height="18" fill="none" stroke="#132334" stroke-width="2.5"/><path d="M5 14 L10 20 L24 3" fill="none" stroke="#132334" stroke-width="4"/></svg>Generators</li>
    <li><svg viewBox="0 0 26 26"><rect x="1.5" y="5.5" width="18" height="18" fill="none" stroke="#132334" stroke-width="2.5"/><path d="M5 14 L10 20 L24 3" fill="none" stroke="#132334" stroke-width="4"/></svg>Service</li>
  </ul>
  <div class="brand">
    <div class="brand__name">Q7M</div>
    <div class="brand__sub">Electrical Systems Inc</div>
  </div>
  <div class="brand-rule"></div>
  <div class="web">q7melectric.com</div>
</section>

<section class="card card--back" aria-label="Business card back">
  <svg class="card__art" viewBox="0 0 600 364" aria-hidden="true">
    <path d="M0,128 Q300,300 600,128 L600,134 Q300,290 0,134 Z" fill="var(--steel)"/>
    <path d="M0,150 Q300,300 600,150 L600,175 Q300,250 0,175 Z" fill="var(--steel)"/>
  </svg>
  <div class="brand">
    <div class="brand__name">Q7M</div>
    <div class="brand__sub">Electrical Systems Inc</div>
  </div>
  <div class="contact">
    <p class="contact__address">482 Harbor Bend #210<br>Lakeview Springs, FL 32790</p>
    <p class="contact__phone"><svg viewBox="0 0 20 20"><rect x="0" y="0" width="20" height="20" rx="5" fill="#9a9a9a"/><path d="M6 4 L8.5 4 L9.5 7 L8 8.3 Q9.3 11 11.7 12 L13 10.5 L16 11.5 L16 14 Q15 16 12.5 15.5 Q6 13.5 4.5 7.5 Q4 5 6 4 Z" fill="#132334"/></svg>407-555-0148</p>
    <p class="contact__email">info@q7melectric.com</p>
  </div>
</section>

</body>
</html>
```